Health Company needs new labels for a new line of natural vitamins and supplements

We are a dutch based health company. We need labels for a new line of healthy, all natural, vitamins and supplements line.
We came across this brand: http://www.velk.eu , we like that style so you can use this as inspiration.
Key words : Natural , Organic logo's , clear , earthy colors , open , trustworthy , healthy
The product should be leading, the logo/brandname can be small, even only mentioned on the rear label.

Health conscious people

Health And Wellness

• A clear , simple, trustworthy , organic style

```html
<!DOCTYPE html>
<html lang="en">
<head>
<meta charset="utf-8">
<title>VELK Natural Vitamin Label</title>
<link href="https://fonts.googleapis.com/css2?family=Montserrat:wght@500;700&display=swap" rel="stylesheet">
<style>
  :root {
    --page-bg: #f2f2f2;
    --fruit-peach: #f6b98a;
    --fruit-orange: #f7a640;
    --fruit-yellow: #f4de5e;
    --fruit-lime: #d8e86a;
    --fruit-pink: #f59a8c;
    --stripe-orange: #ee5a35;
    --band-brown: #4a2a1c;
    --band-green: #4cae14;
    --white: #ffffff;
  }
  html, body {
    margin: 0;
    padding: 0;
    width: 845px;
    height: 1200px;
    overflow: hidden;
    background: var(--page-bg);
  }
  .label {
    position: absolute;
    left: 90px;
    top: 204px;
    width: 666px;
    height: 792px;
    overflow: hidden;
    font-family: "Montserrat", sans-serif;
  }
  .fruit-artwork {
    position: absolute;
    inset: 0 0 96px 0;
    background:
      radial-gradient(circle at 20% 15%, var(--fruit-pink) 0, transparent 30%),
      radial-gradient(circle at 78% 25%, var(--fruit-lime) 0, transparent 32%),
      radial-gradient(circle at 25% 75%, var(--fruit-yellow) 0, transparent 35%),
      radial-gradient(circle at 80% 80%, var(--fruit-orange) 0, transparent 35%),
      linear-gradient(135deg, var(--fruit-peach), var(--fruit-yellow) 55%, var(--fruit-orange));
  }
  .stripe-vertical {
    position: absolute;
    top: 0;
    left: 282px;
    width: 84px;
    height: 696px;
    background: var(--stripe-orange);
    border-left: 8px solid var(--white);
    border-right: 8px solid var(--white);
  }
  .name-band {
    position: absolute;
    left: 0;
    top: 350px;
    width: 100%;
    height: 78px;
    background: var(--band-brown);
    border-top: 6px solid var(--white);
    border-bottom: 6px solid var(--white);
    display: flex;
    align-items: center;
    justify-content: center;
  }
  .brand-name {
    margin-left: 40px;
    color: var(--white);
    font-weight: 500;
    font-size: 38px;
    letter-spacing: 6px;
  }
  .product-band {
    position: absolute;
    left: 0;
    bottom: 0;
    width: 100%;
    height: 96px;
    background: var(--band-green);
    display: flex;
    align-items: center;
    justify-content: center;
  }
  .product-name {
    color: var(--white);
    font-weight: 700;
    font-size: 56px;
    letter-spacing: -0.5px;
    white-space: nowrap;
  }
</style>
</head>
<body>
  <main class="label">
    <div class="fruit-artwork" role="img" aria-label="Soft photo of sliced citrus and mixed fruits in orange, yellow and green tones"></div>
    <div class="stripe-vertical"></div>
    <div class="name-band"><span class="brand-name">VELK</span></div>
    <div class="product-band"><span class="product-name">NATURAL VITAMIN</span></div>
  </main>
</body>
</html>
```